To design a new professional and elegant website design

To design an elegant and professional business website - e.g. Responsive WordPress theme.

Please refer to the existing site www.merrow-partners.example for information regarding the business service and the content that will be included.

While the designer can suggest colors, the current logo (see attached) should remain.
Although I have indicated Sans Serif as a font, I welcome alternative suggestions.
Updates

To all designers:

I have attached additional .psd files of the logo for your use in the design of the new site (theme). As posted in an earlier response, I wish to keep the logo and the color blue. You are welcome to either work with or change the green.

- Please avoid making the page too busy.

- Avoid stock business pictures such as the people working on a document with the calculator the generic people in suits. Ideally, I would like unique media.

- Do not include contact information on the home page. There are two offices – 1 in Houston and one in UK and I want to make sure that we distinguish between the two.

- Use bullets rather than check boxes .

- Do not use the social links as we do not currently use them - this may change in the future

- The footer should include: sitemap, Terms of Use, Privacy Policy and the 2014 Copyright notice. The other pages should be accessible via a menu

Hope this helps.
Thanks

To all participants,

I have increased the budget by an additional £200.

Regards,

Target Market(s)

As you may glean from the website, the company is a management consultancy serving Pinnacle 400 companies and private equity firms. Companies include: Lorn, GQ, TW, Varnell Orbe Companies, Kel Mordan...

Sites that may influence the design include:

http://www.qvd.example.co.uk/consulting/
http://www.jn.example/UK/en/Services/Advisory
http://www.holt.example/industry-expertise/technology/index.aspx
http://www.plovabranding.example/news

Industry/Entity Type

Business Service

Font styles to use
Sans Serif

Colors

Designer to choose colors to be used in the design.

Requirements
Must have
• Existing blue logo - globe with the M & P (see attached). The green is not necessary
Must function of a WordPress responsive platform.
Nice to have
• While the new theme will need to be consistent throughout the site, the home page can vary from the child pages.
Should not have
• Common stock images. If used, the images and icons should be unique.

```html
<!DOCTYPE html>
<html lang="en">
<head>
<meta charset="utf-8">
<title>Merrow Partners</title>
<link href="https://fonts.googleapis.com/css2?family=Open+Sans:wght@300;400;600&display=swap" rel="stylesheet">
<style>
:root{
  --blue:#0b74c6;
  --blue-light:#1b93e0;
  --blue-dark:#0868b5;
  --nav-active:#3a3a3a;
  --text:#555;
  --text-dark:#333;
  --icon:#7a7a7a;
  --rule:#dcdcdc;
  --band:#e8f2f9;
  --footer:#2e2e2e;
  --footer-text:#bdbdbd;
  --gold:#f5a623;
}
*{box-sizing:border-box;margin:0;padding:0}
html,body{width:1089px;height:1200px;overflow:hidden}
body{font-family:'Open Sans',Arial,sans-serif;color:var(--text);background:#fff;position:relative}
.wrap{position:absolute;left:91px;width:908px}

.brand{position:absolute;left:92px;top:22px;display:flex;align-items:center;gap:12px}
.brand-mark{width:60px;height:60px;border-radius:50%;border:5px solid var(--blue)}
.brand-name{font-size:29px;font-weight:400;color:var(--blue);line-height:1.05}

.nav{position:absolute;top:125px;left:0;width:100%;height:45px;background:linear-gradient(var(--blue-light),var(--blue-dark))}
.nav ul{list-style:none;display:flex;position:absolute;left:91px;top:0;height:45px}
.nav li{height:45px;line-height:45px;text-align:center;color:#fff;font-size:13.5px;font-weight:600;border-right:1px solid rgba(0,0,0,.12)}
.nav li.active{background:var(--nav-active)}
.search{position:absolute;left:797px;top:9px;width:202px;height:29px;background:#f4f4f4;font-size:12px;color:#888;line-height:29px;padding-left:10px}
.search svg{position:absolute;right:9px;top:7px}

.hero-band{position:absolute;top:170px;left:0;width:100%;height:368px;background:var(--band)}
.hero{position:absolute;left:90px;top:186px;width:909px;height:337px;background:#0b0b0b;overflow:hidden}
.hero-photo{position:absolute;left:350px;top:0;width:559px;height:337px;background:radial-gradient(ellipse at 60% 50%,#7a7a7a 0%,#444 45%,#141414 85%)}
.hero-copy{position:absolute;left:38px;top:62px;font-size:30px;font-weight:300;color:#eee;line-height:40px}
.hero-copy em{font-style:normal;color:var(--gold)}
.btn{position:absolute;left:40px;top:191px;width:101px;height:32px;background:#ddd;border-radius:2px;color:#333;font-size:15px;line-height:32px;text-align:center}
.dots{position:absolute;left:44px;top:258px;display:flex;gap:5px}

.welcome h2,.expertise h2{font-weight:400;font-size:21px;color:var(--blue);line-height:30px}
.welcome{top:563px}
.welcome .copy{width:680px;margin-top:2px;font-size:12.3px;line-height:21px}
.welcome .copy p{margin-bottom:9px}
.video{position:absolute;left:695px;top:42px;width:213px;height:143px;border-radius:3px;background:radial-gradient(circle at 50% 55%,#3d5c78,#142538 80%)}
.video svg{position:absolute;left:79px;top:44px}

.rule{position:absolute;left:91px;width:908px;height:1px;background:var(--rule)}

.expertise{top:792px}
.grid{position:relative;height:190px}
.item{position:absolute;font-size:15.5px;color:var(--text-dark);line-height:19px}
.item svg{position:absolute;left:0;top:0}
.item span{position:absolute;top:3px;white-space:nowrap}

.clients{position:absolute;top:1050px;left:100px;width:890px;display:flex;justify-content:space-between;align-items:center;font-size:19px;font-weight:400;color:#8a8a8a}

.footer{position:absolute;top:1107px;left:0;width:100%;height:93px;background:var(--footer)}
.footer nav{position:absolute;left:92px;top:20px;font-size:12.5px;color:var(--footer-text)}
.footer nav b{font-weight:400;margin:0 10px}
.footer .copy{position:absolute;left:92px;top:54px;font-size:12px;color:var(--footer-text)}
</style>
</head>
<body>

<header>
  <div class="brand"><div class="brand-mark"></div><div class="brand-name">Merrow<br>Partners</div></div>
</header>

<nav class="nav">
  <ul>
    <li class="active" style="width:83px">HOME</li>
    <li style="width:114px">ABOUT US</li>
    <li style="width:103px">SERVICES</li>
    <li style="width:92px">VALUES</li>
    <li style="width:126px">CONTACT US</li>
    <li style="width:94px">CAREER</li>
    <li style="width:69px">FAQ</li>
  </ul>
  <div class="search">Search
    <svg width="15" height="15" viewBox="0 0 15 15"><circle cx="6" cy="6" r="4.5" fill="none" stroke="#222" stroke-width="2.2"/><line x1="9" y1="9" x2="14" y2="14" stroke="#222" stroke-width="3"/></svg>
  </div>
</nav>

<div class="hero-band"></div>
<section class="hero">
  <div class="hero-photo" role="img" aria-label="Black and white photo of a businessman drawing gears and a growth curve on a grid"></div>
  <h1 class="hero-copy" style="font-weight:300">Where <em>Strategy,</em><br><em>Operations, and People</em><br>deliver performance</h1>
  <div class="btn">Know more</div>
  <div class="dots">
    <svg width="23" height="23" viewBox="0 0 23 23"><circle cx="11.5" cy="11.5" r="10" fill="none" stroke="#888" stroke-width="2"/><path d="M13 7l-4 4.5 4 4.5" fill="none" stroke="#888" stroke-width="2"/></svg>
    <svg width="23" height="23" viewBox="0 0 23 23"><circle cx="11.5" cy="11.5" r="10" fill="none" stroke="#888" stroke-width="2"/><path d="M10 7l4 4.5-4 4.5" fill="none" stroke="#888" stroke-width="2"/></svg>
  </div>
</section>

<section class="wrap welcome">
  <h2>Welcome to Merrow Partners</h2>
  <div class="copy">
    <p>Merrow Partners manages a network of over 300 experienced, independent professionals from diverse industry and functional backgrounds. Our mission is to provide best-of-class, customized advisory services for clients. We address issues relating to top-line growth, cost-optimisation, and other performance issues to build shareholder value.</p>
    <p>We work alongside your teams and leverage our experience to deliver simple but pragmatic solutions to complex business issues at a lower cost than traditional consulting firms. We leave you with a heritage of capabilities and tools needed to sustain results. We combine advisory services with interim managers and executives to provide the most effective support to your businesses needs.</p>
  </div>
  <div class="video" role="img" aria-label="Video still of a person facing a chalkboard growth chart">
    <svg width="56" height="56" viewBox="0 0 56 56"><circle cx="28" cy="28" r="25" fill="none" stroke="#fff" stroke-width="4"/><path d="M22 16l18 12-18 12z" fill="#fff"/></svg>
  </div>
</section>

<div class="rule" style="top:778px"></div>

<section class="wrap expertise">
  <h2>Merrow's Expertise</h2>
  <div class="grid">
    <div class="item" style="left:1px;top:18px"><svg width="32" height="24" viewBox="0 0 32 24" fill="var(--icon)"><circle cx="11" cy="6" r="5"/><circle cx="22" cy="6" r="5"/><path d="M2 24c0-8 4-11 9-11s9 3 9 11zM20 24c0-5-1-8-3-10 8-2 13 2 13 10z"/></svg><span style="left:42px">Due Diligence</span></div>
    <div class="item" style="left:231px;top:18px"><svg width="24" height="24" viewBox="0 0 24 24" fill="var(--icon)"><circle cx="8" cy="8" r="6"/><circle cx="8" cy="8" r="2.5" fill="#fff"/><circle cx="17" cy="17" r="5"/><circle cx="17" cy="17" r="2" fill="#fff"/></svg><span style="left:40px">Strategic Planning</span></div>
    <div class="item" style="left:480px;top:14px"><svg width="32" height="32" viewBox="0 0 32 32" stroke="var(--icon)" stroke-width="3" fill="none"><line x1="4" y1="28" x2="28" y2="4"/><line x1="6" y1="4" x2="28" y2="28"/><circle cx="27" cy="5" r="3"/></svg><span style="left:42px;top:7px">Process Reengineering</span></div>
    <div class="item" style="left:745px;top:16px"><svg width="30" height="28" viewBox="0 0 30 28" fill="none" stroke="var(--icon)" stroke-width="2.5"><rect x="2" y="10" width="16" height="16"/><rect x="12" y="2" width="16" height="16"/></svg><span style="left:41px;top:5px">Portfolio Growth</span></div>

    <div class="item" style="left:4px;top:75px"><svg width="28" height="26" viewBox="0 0 28 26" fill="var(--icon)"><rect x="11" y="0" width="6" height="6"/><rect x="0" y="18" width="6" height="6"/><rect x="11" y="18" width="6" height="6"/><rect x="22" y="18" width="6" height="6"/><rect x="13" y="6" width="2" height="12"/><rect x="2" y="12" width="24" height="2"/></svg><span style="left:38px;top:-6px;white-space:normal;width:130px">Organizational Alignment</span></div>
    <div class="item" style="left:231px;top:75px"><svg width="26" height="26" viewBox="0 0 26 26" fill="var(--icon)"><rect x="0" y="10" width="14" height="14"/><rect x="6" y="5" width="14" height="14" stroke="#fff" stroke-width="1.5"/><rect x="12" y="0" width="14" height="14" stroke="#fff" stroke-width="1.5"/></svg><span style="left:40px;top:4px">Process Automation</span></div>
    <div class="item" style="left:483px;top:75px"><svg width="26" height="26" viewBox="0 0 26 26"><rect x="1" y="1" width="24" height="24" fill="none" stroke="var(--icon)" stroke-width="2"/><rect x="5" y="5" width="16" height="16" fill="var(--icon)"/><text x="13" y="18" font-size="12" fill="#fff" text-anchor="middle" font-family="Arial,sans-serif">$</text></svg><span style="left:39px;top:4px">Cost Reduction</span></div>
    <div class="item" style="left:745px;top:76px"><svg width="32" height="24" viewBox="0 0 32 24" fill="var(--icon)"><circle cx="11" cy="6" r="5"/><circle cx="22" cy="6" r="5"/><path d="M2 24c0-8 4-11 9-11s9 3 9 11zM20 24c0-5-1-8-3-10 8-2 13 2 13 10z"/></svg><span style="left:41px">Governance</span></div>

    <div class="item" style="left:2px;top:145px"><svg width="30" height="22" viewBox="0 0 30 22" fill="var(--icon)"><path d="M7 20a6 6 0 010-12 8 8 0 0115-2 7 7 0 011 14z"/><path d="M15 10v10M11 14l4-4 4 4" stroke="#fff" stroke-width="2" fill="none"/></svg><span style="left:40px;top:2px">Outsourcing</span></div>
    <div class="item" style="left:231px;top:141px"><svg width="28" height="30" viewBox="0 0 28 30" fill="none" stroke="var(--icon)" stroke-width="2"><rect x="2" y="10" width="10" height="19"/><rect x="12" y="2" width="14" height="27"/><path d="M15 6h3M20 6h3M15 11h3M20 11h3M15 16h3M20 16h3M15 21h3M20 21h3M5 14h4M5 19h4M5 24h4"/></svg><span style="left:40px;top:6px">Project Office</span></div>
  </div>
</section>

<div class="rule" style="top:1026px"></div>

<div class="clients">
  <span>Larkmoor</span><span>Quintor</span><span>Netwell</span><span>Brisk</span><span>Tovaro</span><span>Corra</span><span>Halvex</span><span>Adra</span><span>Verlo</span>
</div>

<footer class="footer">
  <nav>Home<b>|</b>About us<b>|</b>Services<b>|</b>Values<b>|</b>Contact us<b>|</b>Career<b>|</b>FAQ<b>|</b>Sitemap<b>|</b>Terms of Use<b>|</b>Privacy Policy</nav>
  <p class="copy">Copyright &copy; 2014 &nbsp;Merrow Partners. &nbsp;All rights reserved.</p>
</footer>

</body>
</html>
```